Take away menu for italian restaurant

We need a brochure for take away. I was thinking about a A4 page with take away for partys on one page and the other with take away for every day. The page with the party menu I want a big very nice food picture. The other site with meals for every day sound be as simple as possible so people do not get too confused over the many different options. so it is very important that it is easy to look at the every day menu. i hope it is possible for you to just use google translate so you know what is what. if not I can try to translate it. but we only need it in danish.

```html
<!DOCTYPE html>
<html lang="da">
<head>
<meta charset="utf-8">
<title>Restaurant Verde – Mad ud af huset</title>
<link rel="stylesheet" href="https://fonts.googleapis.com/css2?family=Source+Sans+3:ital,wght@0,400;0,600;0,700;0,900;1,400&display=swap">
<style>
  :root {
    --paper: #ffffff;
    --canvas: #ffffff;
    --edge: #b9b9b9;
    --ink: #1a1a1a;
    --soft-ink: #3a3a3a;
    --red: #d8231b;
    --green: #1f9a3a;
    --flag-green: #1a9a3e;
    --flag-red: #e0261d;
    --rule: #9a9a9a;
  }
  * { margin: 0; padding: 0; box-sizing: border-box; }
  html, body { width: 1200px; height: 824px; overflow: hidden; background: var(--canvas); }
  body { position: relative; font-family: "Source Sans 3", Arial, sans-serif; color: var(--ink); }

  .page { position: absolute; top: 37px; width: 563px; height: 750px; background: var(--paper); border: 1px solid var(--edge); overflow: hidden; }
  .page--party { left: 33px; }
  .page--everyday { left: 633px; }
  .page > * { position: absolute; }

  .flag { display: flex; width: 82px; height: 27px; }
  .flag span { flex: 1; }
  .flag .g { background: var(--flag-green); }
  .flag .w { background: var(--paper); }
  .flag .r { background: var(--flag-red); }
  .page--party .flag { left: 410px; top: 0; }
  .page--everyday .flag { left: 37px; top: 0; }

  .web { left: 409px; top: 34px; font-size: 11.5px; font-weight: 700; }

  .brand { display: flex; align-items: center; gap: 8px; font-weight: 900; font-size: 28px; letter-spacing: 3px; color: var(--ink); text-transform: uppercase; }
  .brand .mark { width: 13px; height: 13px; background: var(--ink); }
  .page--party .brand { left: 30px; top: 50px; }

  .party-title { left: 38px; top: 114px; width: 160px; font-size: 31px; font-weight: 900; line-height: 33px; }
  .party-intro { left: 210px; top: 118px; width: 132px; font-size: 10px; font-weight: 700; line-height: 13px; }
  .party-price { left: 350px; top: 118px; }
  .party-price strong { display: block; color: var(--green); font-size: 20px; font-weight: 700; line-height: 22px; }
  .party-price em { font-size: 8.5px; font-style: italic; color: var(--soft-ink); }

  .party-details { left: 196px; top: 190px; width: 335px; font-size: 10px; line-height: 12.5px; color: var(--soft-ink); }
  .course-list { list-style: none; }
  .course-list li { position: relative; padding-left: 10px; margin-bottom: 4px; }
  .course-list li::before { content: "•"; position: absolute; left: 0; }
  .bread-note { margin-top: 2px; }
  .sign-off { margin-top: 6px; font-size: 18px; line-height: 20px; font-weight: 700; color: var(--red); }

  .hero-photo { left: 0; top: 350px; width: 563px; height: 400px;
    background: radial-gradient(ellipse 50% 45% at 50% 55%, #d8b48a 0%, #c79a6c 35%, #e9dfd3 70%, rgba(255,255,255,0) 100%),
                linear-gradient(180deg, #ffffff 0%, #eef0ec 30%, #e6e7e3 100%); }

  .backdrop-photo { left: 0; top: 130px; width: 563px; height: 520px; opacity: .45;
    background: radial-gradient(ellipse 60% 50% at 55% 50%, #e8d3b9 0%, #f1e8dd 55%, rgba(255,255,255,0) 100%); }

  .everyday-title { left: 37px; top: 80px; width: 400px; font-size: 25px; font-weight: 700; line-height: 30px; color: var(--red); }
  .everyday-intro { left: 37px; top: 160px; width: 470px; font-size: 10.5px; line-height: 13px; color: var(--green); }

  .menu-col { top: 252px; width: 150px; font-size: 10.5px; line-height: 13px; color: var(--soft-ink); }
  .menu-col--families { left: 37px; }
  .menu-col--packages { left: 190px; }
  .menu-col--single { left: 346px; }
  .menu-col .lead { font-weight: 700; color: var(--ink); margin-bottom: 12px; }
  .menu-col h3 { font-size: 10.5px; font-weight: 700; color: var(--ink); }
  .menu-item { margin-bottom: 12px; }
  .price { color: var(--green); font-weight: 700; }
  .price em { font-weight: 400; }

  .order-more { left: 37px; top: 585px; width: 475px; font-size: 10.5px; line-height: 14px; }
  .order-more strong { font-weight: 700; }

  .footer-rule { left: 37px; top: 643px; width: 475px; height: 1px; background: var(--rule); }
  .page--everyday .brand { left: 37px; top: 656px; font-size: 18px; letter-spacing: 2px; gap: 5px; }
  .page--everyday .brand .mark { width: 9px; height: 9px; }
  .contact { left: 137px; top: 654px; font-size: 9px; line-height: 11px; }
  .contact p { margin-bottom: 8px; }
  .order-note { left: 346px; top: 654px; width: 168px; font-size: 7.5px; line-height: 9.5px; color: var(--soft-ink); }
  .order-note p { margin-bottom: 4px; }
  .page--everyday .web { left: 346px; top: 730px; }
</style>
</head>
<body>

<section class="page page--party">
  <div class="flag"><span class="g"></span><span class="w"></span><span class="r"></span></div>
  <p class="web">www.verde-bistro.dk</p>
  <div class="brand"><span class="mark"></span>Verde</div>

  <h1 class="party-title">5-retters italiensk fest menu</h1>
  <p class="party-intro">Til en dag hvor du ikke orker at kokkerere til dine gæster, men ønsker at give dem en fantastisk madoplevelse. Du sørger selv for hyggen.</p>
  <p class="party-price"><strong>Pris 295 kr.</strong><em>per kuvert (ved min. 10 personer)</em></p>

  <div class="party-details">
    <ul class="course-list">
      <li>Dampet laks på en bund af spæde salatblade med citrus mayonaise</li>
      <li>Cannelloni. Hjemmelavet pastarør fyldt med ricotta og spinat</li>
      <li>Førsteklasses helstegt oksemørbrad på en bund af grønne asparges, hertil små kartofler med koldpresset olivenolie, stave af ovnstegt rodselleri og rødvinssauce</li>
      <li>Et udvalg af italienske oste med valnøddekerner</li>
      <li>Tiramisu; den italienske dessertklassiker med limoncello og skovbær</li>
    </ul>
    <p class="bread-note">Vores hjemmebagt brød med persillepesto får du selvfølgelig også med —</p>
    <p class="sign-off">Buon appetito!</p>
  </div>

  <div class="hero-photo" role="img" aria-label="Foto af risotto-timbale toppet med rejer, kaviar og purløg på hvid tallerken"></div>
</section>

<section class="page page--everyday">
  <div class="backdrop-photo" role="img" aria-label="Svagt baggrundsfoto af italiensk ret"></div>
  <div class="flag"><span class="g"></span><span class="w"></span><span class="r"></span></div>

  <h2 class="everyday-title">Mad ud af huset til hverdag og fest på ægte italiensk manér</h2>
  <p class="everyday-intro">Uanset om det er tirsdag eller lørdag, og om man skal have mange gæster eller bare skal være alene hjemme, kan det være skønt med lidt hjælp til madlavningen. Restaurant Verde kan hjælpe dig med at sørge for maden, så du kun skal sørge for den hjemlige hygge. Vi har forskellige menuer man kan vælge mellem, men hvis man har specialønsker er man selvfølgelig velkommen til at ringe til restauranten og få en snak med vores søde personale.</p>

  <div class="menu-col menu-col--families">
    <p class="lead">Familiepakker Middag til hele familien til en travl dag. Køb en pakke der indeholder nok til to børn og to voksne, der indeholder følgende:</p>
    <div class="menu-item">
      <h3>Familiepakke 1</h3>
      <p>2 x helstegt oksefilet, hertil små rosmarin kartofler, ovnstegte rodfrugter og valgfri sauce.<br>2 x spaghetti bolognese</p>
      <p class="price">Pris kr. 249,-</p>
    </div>
    <div class="menu-item">
      <h3>Familiepakke 2</h3>
      <p>2 x grillet unghanebryst, hertil små kartofler i koldpresset olivenolie, grønne asparges og valgfri sauce.<br>2 x lasagne</p>
      <p class="price">Pris kr. 249,-</p>
    </div>
  </div>

  <div class="menu-col menu-col--packages">
    <p class="lead">Pakker til min. 2 personer Middag til to personer eller flere. Vælg mellem følgende:</p>
    <div class="menu-item">
      <h3>Pakke 1</h3>
      <p>Helstegt oksefilet, hertil små rosmarinkartofler, ovnstegte rodfrugter og valgfri sauce.</p>
    </div>
    <div class="menu-item">
      <h3>Pakke 2</h3>
      <p>Grillet unghanebryst, hertil små kartofler i koldpresset olivenolie, grønne asparges og valgfri sauce.</p>
    </div>
    <div class="menu-item">
      <h3>Pakke 3</h3>
      <p>Penne al filetto; Penne pasta med små stykker af oksemørbrad i fløde-svampe sauce.</p>
    </div>
    <div class="menu-item">
      <h3>Pakke 4</h3>
      <p>Penne al cinghiale; Penne med vildtragout af vildsvin og bacon med frisk revet parmesan.</p>
    </div>
    <p class="price">Pris kun kr. 175,- <em>for to personer</em><br>+ 79 kr. <em>per ekstra kuvert</em></p>
  </div>

  <div class="menu-col menu-col--single">
    <p class="lead">Bestil blot en enkelt ret eller flere. Kan også kombineres med pakkerne. Vælg mellem:</p>
    <div class="menu-item">
      <h3>• Nr. 37.</h3>
      <p>Penne med små stykker af oksemørbrad i fløde-svampe sauce.</p>
      <p class="price">Kr. 99,-</p>
    </div>
    <div class="menu-item">
      <h3>• Nr. 39.</h3>
      <p>Penne med vildtragout af vildsvin og bacon.</p>
      <p class="price">Kr. 99,-</p>
    </div>
    <div class="menu-item">
      <h3>• Nr. 42.</h3>
      <p>Lasagne.</p>
      <p class="price">Kr. 79,-</p>
    </div>
    <div class="menu-item">
      <h3>• Nr. 44.</h3>
      <p>Pastabånd med fersk og røget laks i en cremet spinatsauce.</p>
      <p class="price">Kr. 89,-</p>
    </div>
  </div>

  <p class="order-more">Ønsker de at bestille andre retter fra vores a la carte kort, så ring til os på telefon <strong>86 40 12 57</strong>, udvalg og pris kan du se på <strong>www.verde-bistro.dk</strong></p>

  <div class="footer-rule"></div>
  <div class="brand"><span class="mark"></span>Verde</div>
  <div class="contact">
    <p>Kontakt os<br>Restaurant Verde<br>Kanalgade 14<br>8000 Aarhus C</p>
    <p>Tlf.: 8640 1257<br>Email: kontakt@verde-bistro.dk</p>
  </div>
  <div class="order-note">
    <p>Ved bestilling på 40 personer og derover send da gerne en email eller ring mellem kl. 20-23 eller på hverdage fra kl. 12 og spørg efter Marco.</p>
    <p>Ønsker og allergier kan sendes til:<br>kontakt@verde-bistro.dk</p>
  </div>
  <p class="web">www.verde-bistro.dk</p>
</section>

</body>
</html>
```